Tech Startup Needs Business Card Design

I am looking for an eye catching business card design for our new company, Torn Kite. We are a place for business owners and contractors to share their experiences with their customers and check their current customers. Our website, www.torn-kite.co, may be able to offer some guidance as to the design.

Industry/Entity Type

Business

Contact Information for Business Card

Owen Barthwick
888-417-3083
Owen@torn-kite.co
www.torn-kite.co

```html
<!DOCTYPE html>
<html lang="en">
<head>
<meta charset="utf-8">
<title>Torn Kite — Business Card</title>
<link rel="stylesheet" href="https://fonts.googleapis.com/css2?family=Lato:wght@400;700;900&display=swap">
<style>
  :root {
    --canvas: #ece9e4;
    --card-dark: #2b2b2c;
    --brand-red: #e8242b;
    --ink: #141414;
    --shadow: rgba(0, 0, 0, 0.18);
  }
  * { box-sizing: border-box; margin: 0; padding: 0; }
  html, body {
    width: 1200px;
    height: 1023px;
    overflow: hidden;
    background: var(--canvas);
    font-family: "Lato", Arial, sans-serif;
  }
  .sheet {
    position: relative;
    width: 1200px;
    height: 1023px;
  }
  .card {
    position: absolute;
    left: 300px;
    width: 600px;
    height: 343px;
    border-radius: 4px;
    box-shadow: 0 8px 24px var(--shadow);
    overflow: hidden;
  }
  .card-front { top: 120px; background: var(--card-dark); }
  .card-back  { top: 560px; background: var(--brand-red); }

  .speech-bubble {
    position: absolute;
    left: 0; top: 0;
    width: 600px; height: 343px;
  }
  .contact {
    position: absolute;
    left: 262px;
    top: 56px;
    color: var(--ink);
  }
  .contact-name {
    font-weight: 900;
    font-size: 31px;
    letter-spacing: 0.2px;
    margin-bottom: 12px;
  }
  .contact-line {
    display: flex;
    align-items: center;
    gap: 9px;
    font-size: 17px;
    font-weight: 400;
    line-height: 26px;
  }
  .contact-icon { width: 15px; height: 15px; flex: none; }

  .wordmark {
    position: absolute;
    display: flex;
    align-items: center;
    color: var(--ink);
    font-weight: 700;
    letter-spacing: -0.5px;
    white-space: nowrap;
  }
  .wordmark-dot {
    border-radius: 50%;
    background: var(--brand-red);
    flex: none;
  }
  .card-front .wordmark {
    left: 40px;
    bottom: 34px;
    font-size: 56px;
    gap: 12px;
  }
  .card-front .wordmark-dot { width: 16px; height: 16px; }

  .card-back .wordmark {
    left: 50%;
    top: 50%;
    transform: translate(-50%, -50%);
    font-size: 96px;
    gap: 18px;
  }
  .card-back .wordmark-dot { width: 26px; height: 26px; background: var(--ink); }
</style>
</head>
<body>
<main class="sheet">

  <section class="card card-front" aria-label="Business card front">
    <svg class="speech-bubble" viewBox="0 0 600 343" aria-hidden="true">
      <path fill="#e8242b"
        d="M258 22 H566 Q586 22 586 42 V170 Q586 190 566 190 H530 L548 232 L488 190 H258 Q238 190 238 170 V42 Q238 22 258 22 Z"/>
    </svg>
    <div class="contact">
      <p class="contact-name">Owen Barthwick</p>
      <p class="contact-line">
        <svg class="contact-icon" viewBox="0 0 16 16" aria-hidden="true">
          <path fill="#141414" d="M3.6 1.2l2.3 2.6-1.3 1.9c.9 1.9 2.3 3.3 4.2 4.2l1.9-1.3 2.6 2.3-1.2 2.6C7.1 13.9 2.1 8.9 1 3.9z"/>
        </svg>
        <span>888-417-3083</span>
      </p>
      <p class="contact-line">
        <svg class="contact-icon" viewBox="0 0 16 16" aria-hidden="true">
          <rect x="1" y="3" width="14" height="10" rx="1.5" fill="none" stroke="#141414" stroke-width="1.6"/>
          <path d="M1.8 4 L8 9 L14.2 4" fill="none" stroke="#141414" stroke-width="1.6"/>
        </svg>
        <span>Owen@torn-kite.co</span>
      </p>
    </div>
    <div class="wordmark">
      <span class="wordmark-dot"></span>
      <span class="wordmark-name">torn kite</span>
    </div>
  </section>

  <section class="card card-back" aria-label="Business card back">
    <div class="wordmark">
      <span class="wordmark-dot"></span>
      <span class="wordmark-name">torn kite</span>
    </div>
  </section>

</main>
</body>
</html>
```